21 ERP project mistakes to avoid

I am looking for a document template for a white paper of about 20 pages that discusses 21 mistakes you can make when selecting or implementing erp software. The audience is corporate - typically managers charged with leading an erp selection or implementation project. I want something modern and minimalist. I,m assuming the template would need to be in MS Word but the delivery format would be PDF. This not really a brochure but there is no closer category to this on the site.

Target Market(s)

Corporate enterprise software managers

Font styles to use
Serif
Sans Serif

Colors
0493ce

Requirements
Must have
• Modern,minimalist look. MS Word template or a template I can imoprt text into and convert to PDF for publishing via a web link to the document
Nice to have
• Creative front page and headings for each piece of '21 mistakes' content.plenty of white space in design.
Should not have
• Lots of crammed text and boring headings

```html
<!DOCTYPE html>
<html lang="en">
<head>
<meta charset="utf-8">
<title>21 mistakes you can make when selecting or implementing ERP software</title>
<link rel="stylesheet" href="https://fonts.googleapis.com/css2?family=Lato:wght@400;700;900&display=swap">
<style>
  :root {
    --brand-blue: #2f80c3;
    --deep-blue: #2a78bd;
    --sky-cyan: #12b2e8;
    --accent-orange: #f7a93b;
    --band-green: #566b4f;
    --photo-light: #bfe4f4;
    --photo-mid: #5aa9d6;
    --photo-dark: #1d5f93;
    --paper: #ffffff;
  }
  html, body {
    margin: 0;
    padding: 0;
    overflow: hidden;
  }
  body {
    width: 848px;
    height: 1200px;
    background: var(--paper);
    font-family: "Lato", Arial, sans-serif;
  }
  .cover {
    position: relative;
    width: 848px;
    height: 1200px;
    overflow: hidden;
    background: var(--paper);
  }
  .cover-art {
    position: absolute;
    inset: 0;
    width: 848px;
    height: 1200px;
  }
  .cover-title {
    position: absolute;
    left: 20px;
    top: 738px;
    margin: 0;
    color: var(--brand-blue);
    font-weight: 400;
    line-height: 1;
  }
  .cover-title .line {
    display: block;
    height: 66px;
  }
  .cover-title .key {
    font-size: 49px;
  }
  .cover-title .minor {
    font-size: 24px;
    color: #2b6fae;
  }
  .title-band {
    position: absolute;
    left: 0;
    top: 967px;
    width: 848px;
    height: 104px;
    display: flex;
    align-items: center;
  }
  .title-band .product {
    margin: 0 0 0 54px;
    color: var(--paper);
    font-weight: 700;
    font-size: 101px;
    letter-spacing: 1px;
    line-height: 1;
  }
</style>
</head>
<body>
<main class="cover">
  <svg class="cover-art" viewBox="0 0 919 1300" preserveAspectRatio="none" aria-hidden="false">
    <defs>
      <linearGradient id="photoTone" x1="0" y1="0" x2="1" y2="1">
        <stop offset="0" stop-color="var(--photo-light)"/>
        <stop offset="0.45" stop-color="var(--photo-mid)"/>
        <stop offset="1" stop-color="var(--photo-dark)"/>
      </linearGradient>
    </defs>

    <!-- right-hand blue sweep -->
    <path class="sweep-deep" d="M919,360 C860,600 700,900 400,1300 L919,1300 Z" fill="var(--deep-blue)"/>
    <path class="sweep-cyan" d="M919,395 C850,640 690,930 420,1300 L470,1300 C720,940 870,660 919,470 Z" fill="var(--sky-cyan)"/>
    <path class="sweep-orange" d="M910,400 C840,640 680,930 400,1300" fill="none" stroke="var(--accent-orange)" stroke-width="7"/>

    <!-- lower white sweep -->
    <path class="sweep-white" d="M0,1300 L0,1270 C300,1240 650,1160 919,1150 L919,1300 Z" fill="var(--deep-blue)"/>
    <path class="sweep-white-cut" d="M0,1300 L0,1285 C300,1255 620,1200 919,1185 L919,1300 Z" fill="var(--deep-blue)"/>
    <path d="M0,1280 C320,1250 640,1180 919,1165" fill="none" stroke="var(--accent-orange)" stroke-width="5"/>

    <!-- cover photograph area -->
    <path class="cover-photo" role="img"
          aria-label="Photo: a businessman in a suit pointing at a glowing hexagon grid labelled ERP, Inventory, Product Management, Marketing and Sales, Manufacturing"
          d="M0,0 H919 V375 C820,560 580,760 340,786 C200,800 80,750 0,660 Z"
          fill="url(#photoTone)"/>
    <path class="photo-edge" d="M0,660 C80,750 200,800 340,786 C580,760 820,560 919,375"
          fill="none" stroke="var(--accent-orange)" stroke-width="14"/>

    <!-- title band -->
    <rect class="band-orange" x="0" y="1048" width="470" height="112" fill="var(--accent-orange)"/>
    <rect class="band-green" x="470" y="1048" width="449" height="112" fill="var(--band-green)"/>
  </svg>

  <h1 class="cover-title">
    <span class="line"><span class="key">21 mistakes</span> <span class="minor">you can make when</span></span>
    <span class="line"><span class="key">selecting</span> <span class="minor">or</span></span>
    <span class="line"><span class="key">implementing</span></span>
  </h1>

  <div class="title-band">
    <p class="product">ERP SOFTWARE</p>
  </div>
</main>
</body>
</html>
```